New web page design for our brand Casa Olmera

We have changed our logo and the image of our products, so we would like to redesign ,our web page as well according to the new design.
Our cosmetic products are based in nature and tradition, like they used to be prepared in the old pharmacies.
Our actual web is www.casaolmera.es, so we need similar estructure but completely different design.

Industry/Entity Type

Cosmetics

Number of Pages Required

5+ page

Requirements
Must have
• References to natural ingredients and also to old pharmacys or apothecaries.
Nice to have
• Nature images or old botanics drawings
• I would like to have a cover page with just an image saying welcome to Casa Olmera's world

```html
<!DOCTYPE html>
<html lang="en">
<head>
<meta charset="utf-8">
<title>Casa Olmera</title>
<link href="https://fonts.googleapis.com/css2?family=Playfair+Display:ital,wght@0,400;0,700;1,400&family=Oswald:wght@400;500&family=Open+Sans:wght@400;600&family=Raleway:wght@300;400&display=swap" rel="stylesheet">
<style>
:root{
  --ink:#1e1a17;
  --dark:#262220;
  --darker:#1a1715;
  --nav:#2b2724;
  --amber:#b07a3c;
  --amber-light:#d3a466;
  --amber-dark:#5a3b1f;
  --paper:#ffffff;
  --muted:#9c948c;
  --text:#5b5550;
  --line:#c9c2ba;
  --accent:#8c2a1f;
}
*{box-sizing:border-box;margin:0;padding:0}
html,body{width:876px;height:1200px;overflow:hidden}
body{position:relative;background:linear-gradient(180deg,var(--amber-dark) 0%,var(--amber) 45%,var(--amber-light) 70%,var(--amber) 100%);font-family:'Open Sans',sans-serif;color:var(--text)}
.header{position:absolute;left:0;top:0;width:876px;height:146px;background:radial-gradient(ellipse at 50% 40%,#3d2e22 0%,#221a14 70%,#161210 100%)}
.brand{position:absolute;left:0;width:876px;top:18px;text-align:center;color:#f3ece2}
.brand-name{font-family:'Playfair Display',serif;font-weight:700;font-size:34px;letter-spacing:1px;display:inline-flex;align-items:center;gap:10px}
.brand-name .dot{width:12px;height:12px;border-radius:50%;background:#f3ece2;display:inline-block}
.brand-tag{font-family:'Playfair Display',serif;font-size:11px;letter-spacing:3px;margin-top:4px;color:#d8cbb8;text-transform:uppercase}
.social{position:absolute;right:100px;top:48px;display:flex;gap:6px}
.social span{width:20px;height:20px;border-radius:3px;display:block}
.nav{position:absolute;left:111px;top:122px;width:654px;height:26px;background:var(--nav);display:flex;align-items:center;justify-content:space-around;padding:0 14px;z-index:2}
.nav a{font-family:'Oswald',sans-serif;font-size:11px;color:#e9e2d8;text-decoration:none;letter-spacing:.5px}
.hero{position:absolute;left:0;top:146px;width:876px;height:352px;background:radial-gradient(ellipse at 40% 60%,#c9a27a 0%,#8a6446 40%,#3a2a1f 85%)}
.hero-title{position:absolute;left:455px;top:140px;font-family:'Raleway',sans-serif;font-weight:400;font-size:30px;color:#fff;text-shadow:0 1px 4px rgba(0,0,0,.4)}
.hero-arrow{position:absolute;top:180px;width:14px;height:24px}
.column{position:absolute;left:111px;width:654px}
.welcome{top:502px;height:194px;background:var(--paper);text-align:center;padding:20px 40px 0}
.section-title{font-family:'Playfair Display',serif;font-style:italic;font-size:24px;display:flex;align-items:center;justify-content:center;gap:12px}
.section-title::before,.section-title::after{content:"";width:50px;height:1px;background:currentColor;opacity:.6}
.welcome .section-title{color:var(--ink)}
.welcome p{font-size:8.5px;line-height:1.55;margin:14px auto 0;width:560px;color:var(--text)}
.btn{display:inline-block;background:var(--ink);color:#fff;font-size:8px;padding:5px 12px;margin-top:12px;font-family:'Open Sans',sans-serif}
.products{top:700px;height:252px;background:var(--dark);text-align:center;padding-top:22px;color:#eee}
.products .section-title{color:#f4efe8}
.products .lead{font-size:8.5px;color:#c6beb4;margin-top:10px}
.carousel{position:absolute;left:10px;top:82px;width:634px;height:130px;display:flex;gap:6px}
.feature{width:150px;height:130px;background:#332d29;color:#e8e1d7;text-align:center;padding:14px 12px 0;font-size:8px;line-height:1.5}
.feature h3{font-family:'Playfair Display',serif;font-weight:400;font-size:11px;margin-bottom:8px}
.feature .btn{background:transparent;border:1px solid #aaa;margin-top:8px;padding:3px 10px}
.product{flex:1;height:130px}
.car-arrow{position:absolute;top:140px;width:10px;height:18px}
.footer{position:absolute;left:0;top:966px;width:876px;height:202px;background:var(--darker);color:#cfc7bd}
.fcol{position:absolute;top:18px}
.fcol h4{font-family:'Oswald',sans-serif;font-weight:500;font-size:13px;letter-spacing:.5px;color:#f2ece4;margin-bottom:12px}
.fcol p{font-size:8.5px;line-height:1.6;color:#a9a097}
.contact-row{display:flex;align-items:flex-start;gap:6px;font-size:8.5px;color:#a9a097;margin-bottom:7px;line-height:1.4}
.contact-row svg{flex:none;margin-top:1px}
.newsletter input{display:block;width:150px;height:20px;border:0;background:#f1ede8;font-size:8px;padding:0 6px;margin-bottom:8px;font-family:'Open Sans',sans-serif}
.subscribe{display:inline-block;background:#4a433e;color:#f0e9df;font-size:8px;padding:4px 12px;margin-left:90px}
.bottom{position:absolute;left:0;top:1168px;width:876px;height:32px;background:#100e0d;color:#7d756d;font-size:8px;line-height:32px;padding-left:111px}
</style>
</head>
<body>
<header class="header">
  <div class="brand">
    <div class="brand-name"><span class="dot"></span>Casa Olmera</div>
    <div class="brand-tag">Cosmética tradicional</div>
  </div>
  <div class="social" aria-label="Social links">
    <span style="background:#3b5998"></span>
    <span style="background:#2fa8e0"></span>
    <span style="background:#d64a3a"></span>
    <span style="background:#c4302b"></span>
  </div>
</header>
<nav class="nav">
  <a href="#">HOME</a><a href="#">ABOUT US</a><a href="#">LAB</a><a href="#">PRODUCT LINES</a><a href="#">SERVICES</a><a href="#">NEWS</a><a href="#">CONTACT</a><a href="#">SHOP</a>
  <svg width="10" height="10" viewBox="0 0 10 10"><circle cx="4" cy="4" r="3" fill="none" stroke="#e9e2d8" stroke-width="1.3"/><line x1="6.2" y1="6.2" x2="9" y2="9" stroke="#e9e2d8" stroke-width="1.3"/></svg>
</nav>
<section class="hero" role="img" aria-label="Apothecary jars, mortar and pestle and a lit candle on an old wooden counter">
  <div class="hero-title">Formulas Magistrales</div>
  <svg class="hero-arrow" style="left:14px" viewBox="0 0 14 24"><polyline points="11,2 3,12 11,22" fill="none" stroke="#fff" stroke-width="2"/></svg>
  <svg class="hero-arrow" style="right:14px" viewBox="0 0 14 24"><polyline points="3,2 11,12 3,22" fill="none" stroke="#fff" stroke-width="2"/></svg>
</section>
<section class="column welcome">
  <h2 class="section-title">Welcome to Casa Olmera</h2>
  <p>Our remedies are born in the quiet back room of the old apothecary, where herbs, oils and waxes were weighed by hand and blended with patience. We keep that craft alive today, choosing natural ingredients from local growers and preparing every cream, balm and tonic in small batches, just as the master pharmacists of old taught us.</p>
  <span class="btn">Read more</span>
</section>
<section class="column products">
  <h2 class="section-title">Our Products</h2>
  <p class="lead">Discover our blends of botanicals, waxes and essences, each prepared with patience, care and tradition.</p>
  <div class="carousel">
    <div class="feature">
      <h3>Premium Line</h3>
      Facial balms and body oils crafted from cold-pressed seeds and wild herbs, following recipes kept in our old ledgers.
      <br><span class="btn">Read More</span>
    </div>
    <div class="product" role="img" aria-label="Amber glass bottles of body oil" style="background:linear-gradient(160deg,#f2ece4,#c98a3e)"></div>
    <div class="product" role="img" aria-label="Small amber bottles with labels" style="background:linear-gradient(160deg,#f6f2ec,#b37536)"></div>
    <div class="product" role="img" aria-label="Labelled product box with a jar" style="background:linear-gradient(160deg,#ffffff,#9a8d80)"></div>
    <div class="product" role="img" aria-label="Cosmetic jars and bottles with herbs" style="background:linear-gradient(160deg,#e9e4da,#7d8a55)"></div>
  </div>
  <svg class="car-arrow" style="left:-2px" viewBox="0 0 10 18"><polyline points="8,2 2,9 8,16" fill="none" stroke="#ccc" stroke-width="1.6"/></svg>
  <svg class="car-arrow" style="right:-2px" viewBox="0 0 10 18"><polyline points="2,2 8,9 2,16" fill="none" stroke="#ccc" stroke-width="1.6"/></svg>
</section>
<footer class="footer">
  <div class="fcol" style="left:111px;width:200px">
    <h4>WHO WE ARE</h4>
    <p>A family workshop that brings the wisdom of the old village pharmacy to everyday care, with honest formulas and ingredients we know by name.</p>
  </div>
  <div class="fcol" style="left:395px;width:190px">
    <h4>Contact Us</h4>
    <div class="contact-row"><svg width="8" height="10" viewBox="0 0 8 10"><path d="M4 0a3.5 3.5 0 0 1 3.5 3.5C7.5 6 4 10 4 10S.5 6 .5 3.5A3.5 3.5 0 0 1 4 0z" fill="#a9a097"/><circle cx="4" cy="3.5" r="1.3" fill="#1a1715"/></svg><span>Calle del Romero 14, Local 2<br>28004 Madrid, España</span></div>
    <div class="contact-row"><svg width="9" height="9" viewBox="0 0 10 10"><path d="M2 0.5l2 2.2-1 1.3a6 6 0 0 0 3 3l1.3-1 2.2 2-1.2 1.5C4.5 9.5.5 5.5 0.5 1.7z" fill="#a9a097"/></svg><span>+34 910 000 000</span></div>
    <div class="contact-row"><svg width="10" height="8" viewBox="0 0 10 8"><rect x=".5" y=".5" width="9" height="7" fill="none" stroke="#a9a097"/><polyline points=".5,.5 5,4.5 9.5,.5" fill="none" stroke="#a9a097"/></svg><span>hola@casaolmera.es</span></div>
  </div>
  <div class="fcol newsletter" style="left:610px;width:160px">
    <h4>Newsletter</h4>
    <input type="text" placeholder="Your email">
    <span class="subscribe">Subscribe</span>
  </div>
</footer>
<div class="bottom">© 2024 Casa Olmera. All rights reserved.</div>
</body>
</html>
```